Banner Ad Design for Velvet Aisle Boutique

Are you a Stylish Designer? Can you work with a balanced color wheel? Let your creative juices flow this way!

```html
<!DOCTYPE html>
<html lang="en">
<head>
<meta charset="utf-8">
<title>Velvet Aisle Boutique – Bridal Lingerie Banner</title>
<link rel="stylesheet" href="https://fonts.googleapis.com/css2?family=Cinzel:wght@400&family=Parisienne&display=swap">
<style>
  :root {
    --blush: #f7d3cb;
    --blush-deep: #f2c2b8;
    --blush-light: #fbe6e0;
    --mauve: #c4838f;
    --mauve-text: #c7929a;
    --white: #ffffff;
    --ornament-a: #f6dcd6;
    --ornament-b: #e9b7bd;
    --figure-a: #f3d0c8;
    --figure-b: #e3a9a6;
  }
  html, body {
    margin: 0;
    padding: 0;
    overflow: hidden;
    background: var(--blush);
  }
  .banner {
    position: relative;
    width: 1200px;
    height: 290px;
    overflow: hidden;
    background: linear-gradient(90deg, var(--blush-deep) 0%, var(--blush) 55%, var(--blush-deep) 100%);
  }
  .banner__glow {
    position: absolute;
    inset: 0;
  }
  .banner__ornament {
    position: absolute;
    left: 0;
    top: 0;
    width: 240px;
    height: 290px;
    background: radial-gradient(ellipse at 35% 60%, var(--ornament-b) 0%, var(--ornament-a) 45%, rgba(246,220,214,0) 75%);
  }
  .banner__figure {
    position: absolute;
    right: 0;
    top: 0;
    width: 234px;
    height: 290px;
    background: linear-gradient(180deg, var(--figure-a) 0%, var(--figure-b) 55%, var(--figure-a) 100%);
  }
  .banner__title {
    position: absolute;
    left: 0;
    width: 1290px;
    top: 22px;
    margin: 0;
    text-align: center;
    font-family: "Cinzel", serif;
    font-weight: 400;
    font-size: 64px;
    letter-spacing: 1px;
    color: var(--white);
    line-height: 1;
  }
  .banner__title .small {
    font-size: 50px;
  }
  .banner__tagline {
    position: absolute;
    left: 0;
    width: 1210px;
    top: 92px;
    margin: 0;
    text-align: center;
    font-family: "Parisienne", cursive;
    font-weight: 400;
    font-size: 70px;
    color: var(--mauve-text);
    line-height: 1.2;
  }
  .banner__cta {
    position: absolute;
    left: 580px;
    top: 210px;
    width: 328px;
    height: 48px;
    box-sizing: border-box;
    border: 3px solid var(--white);
    border-radius: 26px;
    background: var(--mauve);
    color: var(--white);
    font-family: "Parisienne", cursive;
    font-size: 34px;
    line-height: 42px;
    text-align: center;
    text-decoration: none;
  }
</style>
</head>
<body>
  <div class="banner">
    <svg class="banner__glow" width="1200" height="290" viewBox="0 0 1200 290" aria-hidden="true">
      <path d="M0 0 H980 C820 40 620 150 330 230 C200 265 90 280 0 290 Z" fill="var(--blush-light)" opacity="0.7"/>
      <path d="M0 0 H760 C560 60 360 150 150 200 C90 214 40 222 0 226 Z" fill="var(--white)" opacity="0.25"/>
    </svg>

    <div class="banner__ornament" role="img" aria-label="Flowing floral swirl ornament with a tulip bud"></div>

    <h1 class="banner__title">B<span class="small">RIDAL</span> L<span class="small">INGERIE</span></h1>
    <p class="banner__tagline">Gorgeous, sweet &amp; petite!</p>
    <a class="banner__cta" href="#catalogue">view catalogue</a>

    <div class="banner__figure" role="img" aria-label="Model torso wearing a pink corset with garters and stockings"></div>
  </div>
</body>
</html>
```